KTNW Unique Letterhead for Financial Services Business

I am looking for a letterhead design to match our branding colours. I do not want to see anything generic that could be created in word, I can do that myself, I am after something with a bit of designer flair. Once completed I will need files in a print ready format (including bleed area).

I have included our logo file and also our new business card design but get creative.

Industry/Entity Type

Financial Services

Font styles to use
Other font styles liked:
• raleway

Colors
00AB8E
00BBA5
67D7C9
C6EFE9
E9F9F6

Requirements
Must have
• Must be consisten with logo branding colours.
Should not have
• Anything generic that I could create myself in word

```html
<!DOCTYPE html>
<html lang="en">
<head>
<meta charset="utf-8">
<title>KTNW Financial Services Letterhead</title>
<link href="https://fonts.googleapis.com/css2?family=Montserrat:wght@400;700&family=Open+Sans:wght@600&family=Questrial&family=Roboto:wght@400&display=swap" rel="stylesheet">
<style>
  :root {
    --backdrop: #3e3e3e;
    --paper: #e4e4e4;
    --teal-dark: #0a6f78;
    --teal: #0d8a8a;
    --teal-light: #12a596;
    --grey-band: #a7a7aa;
    --ink: #555558;
    --ink-soft: #626266;
    --rule: #8a8a8a;
  }
  * { margin: 0; padding: 0; box-sizing: border-box; }
  html, body { width: 1119px; height: 1200px; overflow: hidden; background: var(--backdrop); }
  .letterhead {
    position: absolute; left: 134px; top: 20px; width: 851px; height: 1160px;
    background: var(--paper); color: var(--ink); overflow: hidden;
    font-family: "Questrial", sans-serif;
  }
  .header-wave { position: absolute; left: 0; top: 0; width: 851px; height: 178px; }
  .brand { position: absolute; left: 38px; top: 70px; width: 210px; text-align: center; }
  .brand-name {
    display: flex; align-items: center; justify-content: center; gap: 8px;
    font-family: "Montserrat", sans-serif; font-weight: 400; font-size: 25px;
    letter-spacing: 1px; color: var(--teal-dark); line-height: 1;
  }
  .brand-dot { width: 14px; height: 14px; background: var(--teal-dark); }
  .brand-tagline {
    margin-top: 4px; font-family: "Montserrat", sans-serif; font-size: 10.5px;
    letter-spacing: 5.5px; color: var(--ink-soft);
  }
  .postal {
    position: absolute; right: 36px; top: 76px; text-align: right;
    font-family: "Montserrat", sans-serif; font-size: 15.5px; line-height: 23px; color: var(--ink);
    display: flex; gap: 6px; align-items: flex-start;
  }
  .postal svg { width: 16px; height: 20px; margin-top: 1px; }
  .recipient { position: absolute; left: 39px; top: 270px; font-family: "Montserrat", sans-serif; }
  .recipient-name { font-weight: 700; font-size: 26px; color: var(--teal-dark); letter-spacing: .5px; line-height: 1.1; }
  .recipient-detail { font-size: 14.5px; color: var(--ink-soft); margin-top: 9px; line-height: 20px; }
  .letter-date {
    position: absolute; right: 36px; top: 378px;
    font-family: "Open Sans", sans-serif; font-weight: 600; font-size: 15.5px; color: var(--ink-soft);
  }
  .letter-body {
    position: absolute; left: 34px; top: 433px; width: 781px;
    font-size: 14.2px; line-height: 19.1px; text-align: justify; color: var(--ink-soft);
  }
  .letter-body p { margin-bottom: 19px; }
  .letter-body p.tight { margin-bottom: 0; }
  .letter-body p.spaced { margin-top: 38px; }
  .signoff { position: absolute; right: 54px; top: 823px; font-size: 20px; color: var(--ink-soft); }
  .signature-area {
    position: absolute; left: 620px; top: 867px; width: 170px; height: 96px;
    background: linear-gradient(135deg, #d6d6d6, #cfcfcf); border-radius: 4px;
  }
  .contact-footer {
    position: absolute; left: 34px; top: 1061px;
    font-family: "Roboto", sans-serif; font-size: 11.7px; color: var(--ink);
  }
  .contact-row { display: flex; align-items: center; gap: 6px; height: 23px; }
  .contact-row svg { width: 13px; height: 13px; }
  .footer-rule { position: absolute; left: 316px; right: 0; top: 1116px; border-top: 1px solid var(--rule); }
</style>
</head>
<body>
<main class="letterhead">
  <svg class="header-wave" viewBox="0 0 1055 220" preserveAspectRatio="none" aria-hidden="true">
    <defs>
      <linearGradient id="waveTeal" x1="0" y1="1" x2="1" y2="0">
        <stop offset="0" stop-color="#14a99a"/>
        <stop offset=".45" stop-color="#0d8f8c"/>
        <stop offset="1" stop-color="#075f70"/>
      </linearGradient>
      <linearGradient id="waveGrey" x1="0" y1="0" x2="1" y2="0">
        <stop offset="0" stop-color="#c4c4c6"/>
        <stop offset=".5" stop-color="#a3a3a6"/>
        <stop offset="1" stop-color="#8d8d92"/>
      </linearGradient>
    </defs>
    <path d="M0 178 C120 205 260 200 420 170 C640 125 780 40 1055 12 L1055 22 C800 45 650 140 420 182 C260 210 110 212 0 190 Z" fill="url(#waveGrey)"/>
    <path d="M150 193 C330 180 430 80 540 0 L1055 0 L1055 10 C860 18 720 70 560 135 C430 182 300 196 150 193 Z" fill="url(#waveTeal)"/>
  </svg>

  <div class="brand">
    <div class="brand-name"><span class="brand-dot"></span>KTNW</div>
    <div class="brand-tagline">Financial Services</div>
  </div>

  <div class="postal">
    <div>PO Box 4810 Ridgeview<br>NSW 2390</div>
    <svg viewBox="0 0 16 20" aria-hidden="true">
      <path d="M8 1a6 6 0 0 0-6 6c0 4.5 6 10 6 10s6-5.5 6-10a6 6 0 0 0-6-6z" fill="var(--teal)"/>
      <circle cx="8" cy="7" r="2.3" fill="var(--paper)"/>
      <ellipse cx="8" cy="18.3" rx="5" ry="1.2" fill="none" stroke="var(--teal)" stroke-width="1"/>
    </svg>
  </div>

  <section class="recipient">
    <h1 class="recipient-name">MARA ELLISON</h1>
    <p class="recipient-detail">0123-456-789</p>
    <p class="recipient-detail" style="margin-top:7px">info@youremailaddress.com</p>
    <p class="recipient-detail" style="margin-top:7px">58 Harbour Ln. Suite<br>12 Kingsford, NSW 2032</p>
  </section>

  <p class="letter-date">12 December, 2023</p>

  <article class="letter-body">
    <p>Lorem ipsum dolor sit amet, consectetuer adipiscing elit, sed diam nonummy nibh euismod tincidunt ut laoreet dolore magna aliquam erat volutpat. Ut wisi enim ad minim veniam, quis nostrud exerci tation ullamcorper suscipit lobortis nisl ut aliquip ex ea commodo consequat. Duis autem vel eum iriure dolor in hendrerit in vulputate velit esse molestie consequat, vel illum dolore eu feugiat nulla facilisis at vero eros et accumsan et iusto odio dignissim qui blandit praesent luptatum zzril delenit augue duis dolore te feugait nulla facilisi.</p>
    <p class="tight">Lorem ipsum dolor sit amet, cons ectetuer adipiscing elit, sed diam nonummy nibh euismod tincidunt ut laoreet dolore magna aliquam erat volutpat. Ut wisi enim ad minim veniam, quis nostrud exerci tation ullamcorper suscipit lobortis nisl ut aliquip ex ea commodo consequat.</p>
    <p class="tight">Lorem ipsum dolor sit amet, consectetuer adipiscing elit, sed diam nonummy nibh euismod tincidunt ut laoreet dolore magna aliquam erat</p>
    <p class="spaced">Lorem ipsum dolor sit amet, cons ectetuer adipiscing elit, sed diam nonummy nibh euismod tincidunt ut laoreet dolore magna aliquam erat volutpat. Ut wisi enim ad minim veniam, quis nostrud exerci tation ullamcorper suscipit lobortis nisl ut aliquip ex ea commodo consequat. Lorem ipsum dolor sit zamet, consectetuer adipiscing elit, sed diam nonummy nibh euismod tincidunt.</p>
  </article>

  <p class="signoff">Managing Director</p>
  <div class="signature-area" role="img" aria-label="Handwritten signature of the managing director"></div>

  <footer class="contact-footer">
    <div class="contact-row">
      <svg viewBox="0 0 14 14" aria-hidden="true"><circle cx="7" cy="7" r="7" fill="var(--teal)"/><path d="M4.3 3.6l1.3-.3.8 1.8-.8.7c.4.9 1 1.6 1.9 2l.7-.8 1.8.8-.3 1.3c-3 .4-5.8-2.4-5.4-5.5z" fill="#fff"/></svg>
      <span>0400 318 562</span>
    </div>
    <div class="contact-row">
      <svg viewBox="0 0 14 14" aria-hidden="true"><circle cx="7" cy="7" r="7" fill="var(--teal)"/><rect x="3.5" y="4.5" width="7" height="5" fill="#fff"/><path d="M3.5 4.5L7 7.4l3.5-2.9" fill="none" stroke="var(--teal)" stroke-width=".9"/></svg>
      <span>info@ktnwfinancial.com.au</span>
    </div>
    <div class="contact-row">
      <svg viewBox="0 0 14 14" aria-hidden="true"><circle cx="7" cy="7" r="7" fill="var(--teal)"/><g fill="none" stroke="#fff" stroke-width=".8"><circle cx="7" cy="7" r="4.2"/><ellipse cx="7" cy="7" rx="1.8" ry="4.2"/><path d="M2.8 7h8.4M3.5 5h7M3.5 9h7"/></g></svg>
      <span>www.ktnwfinancial.com.au</span>
    </div>
  </footer>
  <div class="footer-rule"></div>
</main>
</body>
</html>
```